Long Established Local Fencing (not swords) Business needs fresh Business Cards

We need fresh double sided business cards for our Fencing Construction business, we are looking for something with our new logo design added, and maybe a photo background ?
We recently had cards made from Cardlyne and we were horrified with what we got back, the quality was terrible, so am looking for high quality format for good printing company to make.
We install Steelmora, Timber paling, Aluminium Slat Screening, Picket (timber and aluminium) and most other fencing installations.
Our website is brankelrails.com.au should you like to learn a bit more.
We do have logo in other formats if required.
We have been in business for over 35 years and we have used this as a "motto" it is on our signage

Industry/Entity Type

Construction

Contact Information for Business Card

Open to ideas, we need 3 x different cards, one generic with no name and 2 x others each with 1 of our bosses name on each, I will put into upload files.

Colors
ec1f27
000000
606060
f5f5f5

Requirements
Must have
• Company Name and Logo
• Address
• Contact details, phone, website, email etc
• Small space to write notes when leaving card at residence
Nice to have
• Our motto "Servicing the Peninsula for over 35 years"

```html
<!DOCTYPE html>
<html lang="en">
<head>
<meta charset="utf-8">
<title>Brankel Rails – Business Cards</title>
<link rel="stylesheet" href="https://fonts.googleapis.com/css2?family=Montserrat:wght@400;500;600;700&display=swap">
<style>
  :root {
    --stage: #c9c9c9;
    --card: #231f20;
    --red: #e1302f;
    --white: #ffffff;
    --cream: #f1ecc4;
    --text: #f5f5f5;
    --sky: #dfe8ee;
    --fence-blue: #2b3a5c;
    --fence-green: #6f8a78;
  }
  * { margin: 0; padding: 0; box-sizing: border-box; }
  html, body { width: 1200px; height: 900px; overflow: hidden; }
  body {
    background: var(--stage);
    font-family: "Montserrat", Arial, sans-serif;
    position: relative;
  }
  .card {
    position: absolute;
    top: 297px;
    width: 510px;
    height: 307px;
    background: var(--card);
    overflow: hidden;
    color: var(--text);
  }
  .card--front { left: 59px; }
  .card--back { left: 626px; }
  .card__art { position: absolute; inset: 0; }

  .brand {
    position: absolute;
    display: flex;
    flex-direction: column;
    align-items: center;
    color: var(--white);
    font-weight: 700;
    text-transform: uppercase;
    line-height: 1;
  }
  .brand__dot { border-radius: 50%; background: var(--red); }
  .card--front .brand { left: 325px; top: 88px; width: 160px; }
  .card--front .brand__dot { width: 54px; height: 54px; margin-bottom: 24px; }
  .card--front .brand__name { font-size: 26px; text-align: center; letter-spacing: 1px; }
  .rule {
    position: absolute; left: 333px; top: 222px; width: 140px; height: 1.5px;
    background: var(--white);
  }
  .motto {
    position: absolute; left: 300px; top: 235px; width: 210px;
    text-align: center; font-size: 14.5px; line-height: 21px; color: var(--cream);
  }
  .motto__years { color: var(--red); font-weight: 600; }

  .card--back .brand { right: 28px; top: 16px; align-items: center; }
  .card--back .brand__dot { width: 26px; height: 26px; margin-bottom: 6px; }
  .card--back .brand__name { font-size: 11px; letter-spacing: .5px; }

  .contact {
    position: absolute; right: 26px; top: 88px;
    display: flex; flex-direction: column; align-items: flex-end;
  }
  .contact__name { color: var(--red); font-size: 19px; letter-spacing: .5px; margin-bottom: 14px; }
  .contact__line { display: flex; align-items: center; gap: 7px; font-size: 13px; }
  .contact__address { display: flex; align-items: center; gap: 7px; margin-bottom: 10px; }
  .contact__address p { font-size: 13px; line-height: 20px; text-align: right; }
  .contact__phone { font-size: 19px; font-weight: 600; margin-bottom: 10px; }
  .contact__web { margin-bottom: 12px; }
  .icon { width: 11px; height: 11px; flex: none; fill: var(--red); }
  .notes {
    position: absolute; left: 30px; top: 282px; width: 436px;
    border-top: 1.5px dashed #bdbdbd;
  }
  .notes__pin { position: absolute; right: 26px; top: 275px; }
</style>
</head>
<body>

<section class="card card--front" aria-label="Card front">
  <svg class="card__art" viewBox="0 0 510 307" aria-hidden="false">
    <path d="M0 180 C10 250 60 300 120 307 L0 307 Z" fill="var(--red)"/>
    <path d="M0 0 H300 C365 10 360 140 280 215 C210 285 80 312 0 290 Z" fill="var(--red)"/>
    <path d="M0 0 H270 C345 10 345 135 270 205 C205 268 95 285 20 272 L0 268 Z" fill="var(--white)"/>
    <path role="img" aria-label="Photo of a dark blue steel fence in front of a house with a palm tree"
      d="M0 0 H255 C330 12 328 130 258 196 C198 252 100 268 45 260 L0 250 Z"
      fill="url(#frontPhoto)"/>
    <defs>
      <linearGradient id="frontPhoto" x1="0" y1="0" x2="0" y2="1">
        <stop offset="0" stop-color="#5e6f86"/>
        <stop offset=".32" stop-color="#c9d3d8"/>
        <stop offset=".36" stop-color="var(--fence-blue)"/>
        <stop offset="1" stop-color="#1f2b45"/>
      </linearGradient>
    </defs>
  </svg>
  <div class="brand">
    <span class="brand__dot"></span>
    <span class="brand__name">Brankel<br>Rails</span>
  </div>
  <span class="rule"></span>
  <p class="motto">Servicing the Peninsula<br>for over <span class="motto__years">35</span> years</p>
</section>

<section class="card card--back" aria-label="Card back">
  <svg class="card__art" viewBox="0 0 510 307">
    <path d="M0 150 C5 220 50 262 120 258 C60 250 20 215 0 150 Z" fill="var(--red)"/>
    <path d="M0 0 H240 C295 10 300 130 230 200 C170 258 70 268 0 245 Z" fill="var(--red)"/>
    <path d="M0 0 H225 C282 12 284 125 220 190 C160 245 70 252 0 232 Z" fill="var(--white)"/>
    <path role="img" aria-label="Photo of a green steel fence with cream lattice top along a grassy yard"
      d="M0 0 H210 C265 15 266 122 208 180 C152 232 70 238 0 222 Z"
      fill="url(#backPhoto)"/>
    <defs>
      <linearGradient id="backPhoto" x1="0" y1="0" x2="0" y2="1">
        <stop offset="0" stop-color="var(--sky)"/>
        <stop offset=".2" stop-color="#e9e4d2"/>
        <stop offset=".3" stop-color="var(--fence-green)"/>
        <stop offset=".85" stop-color="#5a7463"/>
        <stop offset="1" stop-color="#4d6a3a"/>
      </linearGradient>
    </defs>
  </svg>
  <div class="brand">
    <span class="brand__dot"></span>
    <span class="brand__name">Brankel Rails</span>
  </div>
  <div class="contact">
    <h2 class="contact__name" style="font-weight:400">DORIAN FALKE</h2>
    <div class="contact__address">
      <p>27 Lorne Street<br>Brankel Bay, Nsw 2290</p>
      <svg class="icon" viewBox="0 0 12 12"><path d="M6 0a4 4 0 0 0-4 4c0 3 4 8 4 8s4-5 4-8a4 4 0 0 0-4-4zm0 5.5A1.5 1.5 0 1 1 6 2.5a1.5 1.5 0 0 1 0 3z"/></svg>
    </div>
    <div class="contact__line contact__phone">02 5550 1847
      <svg class="icon" viewBox="0 0 12 12"><path d="M2.5 0.5l2 2.5-1.2 1.3a7 7 0 0 0 4.4 4.4L9 7.5l2.5 2-1.2 2C5 11.5.5 7 .5 1.7z"/></svg>
    </div>
    <div class="contact__line contact__web">brankelrails.com.au
      <svg class="icon" viewBox="0 0 12 12"><circle cx="6" cy="6" r="5.5"/><path d="M.5 6h11M6 .5c-3 3-3 8 0 11M6 .5c3 3 3 8 0 11" stroke="var(--card)" fill="none"/></svg>
    </div>
    <div class="contact__line">brankelrails@mailbay.com
      <svg class="icon" viewBox="0 0 12 12"><rect y="2" width="12" height="8" rx="1"/><path d="M0 2.5l6 4 6-4" stroke="var(--card)" fill="none"/></svg>
    </div>
  </div>
  <span class="notes" aria-label="Space for notes"></span>
  <svg class="icon notes__pin" viewBox="0 0 12 12"><path d="M6 0a4 4 0 0 0-4 4c0 3 4 8 4 8s4-5 4-8a4 4 0 0 0-4-4zm0 5.5A1.5 1.5 0 1 1 6 2.5a1.5 1.5 0 0 1 0 3z"/></svg>
</section>

</body>
</html>
```